Growing cleaning business needs catchy residential postcard promo

Business has a new website. We are growing and expanding but trying to catch the attention of higher end customers. We are competing with local franchises and some other mom and pop businesses. The design should stand out to show we are providing high quality service every time. Would like to use similar color scheme as the website,

Target Market(s)

Professionals, Busy Moms, anybody who is looking for a quality service

Industry/Entity Type

Business

Requirements
Must have
• Nice details, some picture and catchy phrases

```html
<!DOCTYPE html>
<html lang="en">
<head>
<meta charset="utf-8">
<title>Tidy Nest Postcard</title>
<link rel="stylesheet" href="https://fonts.googleapis.com/css2?family=Lobster&family=Lato:wght@400;700&family=Cinzel:wght@400;700&display=swap">
<style>
  :root {
    --backdrop: #3a3a3a;
    --sky: #1a9be0;
    --sky-deep: #0f6fc0;
    --orange: #f7941d;
    --orange-deep: #f26c1e;
    --green: #8dc63f;
    --green-deep: #6aa42f;
    --ink: #333333;
    --grey-ink: #555555;
    --white: #ffffff;
    --stamp: #d4d4d4;
  }
  * { margin: 0; padding: 0; box-sizing: border-box; }
  html, body { width: 907px; height: 1200px; overflow: hidden; }
  body { background: var(--backdrop); font-family: "Lato", sans-serif; position: relative; }

  .postcard { position: absolute; left: 75px; width: 758px; height: 490px; background: var(--white); overflow: hidden; }
  .postcard--front { top: 88px; }
  .postcard--back { top: 619px; }
  .postcard svg.shapes { position: absolute; inset: 0; }

  .headline { position: absolute; font-family: "Lobster", cursive; line-height: 1; }
  .headline--white { left: 30px; top: 18px; font-size: 52px; color: var(--white); }
  .headline--orange { left: 30px; top: 84px; font-size: 46px; color: var(--orange); }
  .services-title { position: absolute; left: 25px; top: 306px; font-family: "Lobster", cursive; font-size: 19px; line-height: 1.3; color: var(--green-deep); }
  .services-copy { position: absolute; left: 25px; top: 366px; width: 390px; font-size: 12px; line-height: 1.3; color: var(--ink); text-align: justify; }
  .front-web { position: absolute; left: 25px; top: 457px; font-size: 15px; letter-spacing: 7.6px; color: var(--white); }

  .brand { position: absolute; display: flex; align-items: center; gap: 10px; }
  .brand__dot { width: 30px; height: 30px; border-radius: 50%; background: var(--green); flex: none; }
  .brand__name { font-family: "Lato", sans-serif; font-weight: 700; font-size: 30px; color: var(--sky-deep); line-height: 1; }
  .brand__tag { font-family: "Lato", sans-serif; font-weight: 700; font-size: 30px; color: var(--sky-deep); }
  .brand--front { left: 440px; top: 405px; }
  .brand--back { left: 72px; top: 40px; }
  .brand-sub { position: absolute; font-family: "Cinzel", serif; font-size: 10px; color: var(--sky-deep); letter-spacing: .5px; }
  .brand-sub--front { left: 520px; top: 440px; }
  .brand-sub--back { left: 152px; top: 76px; }

  .offer { position: absolute; left: 28px; top: 150px; font-family: "Lobster", cursive; font-size: 28px; color: var(--white); }
  .offer span { color: var(--orange); }
  .service-label { position: absolute; top: 359px; font-family: "Cinzel", serif; font-size: 13px; color: var(--white); letter-spacing: .6px; }
  .service-label--home { left: 28px; }
  .service-label--office { left: 243px; }
  .estimate { position: absolute; left: 28px; top: 394px; font-family: "Cinzel", serif; font-size: 22px; color: var(--grey-ink); letter-spacing: .5px; }
  .estimate span { color: var(--sky-deep); }
  .contact-line { position: absolute; left: 28px; top: 449px; font-size: 17px; font-weight: 700; color: var(--white); display: flex; gap: 32px; }
</style>
</head>
<body>

<section class="postcard postcard--front">
  <svg class="shapes" width="758" height="490" viewBox="0 0 758 490">
    <defs>
      <linearGradient id="skyFill" x1="0" y1="0" x2="1" y2="1">
        <stop offset="0" stop-color="#29b3ec"/>
        <stop offset="1" stop-color="#0f6fc0"/>
      </linearGradient>
      <linearGradient id="roomFill" x1="0" y1="0" x2="0" y2="1">
        <stop offset="0" stop-color="#f1ede6"/>
        <stop offset=".6" stop-color="#d9cdbd"/>
        <stop offset="1" stop-color="#b79d7e"/>
      </linearGradient>
      <linearGradient id="whiteFade" x1="0" y1="0" x2="0" y2="1">
        <stop offset="0" stop-color="#ffffff"/>
        <stop offset="1" stop-color="#ececec"/>
      </linearGradient>
    </defs>
    <rect width="758" height="490" fill="url(#whiteFade)"/>
    <path d="M0 0 H430 V210 Q220 200 0 300 Z" fill="url(#skyFill)"/>
    <path d="M0 300 Q220 200 430 212" fill="none" stroke="var(--orange)" stroke-width="6"/>
    <g role="img" aria-label="Bright modern living room with sofa, rug and large windows">
      <circle cx="560" cy="185" r="195" fill="url(#roomFill)"/>
    </g>
    <circle cx="560" cy="185" r="195" fill="none" stroke="var(--orange)" stroke-width="6"/>
    <g role="img" aria-label="Bottles of cleaning products and sponges">
      <circle cx="65" cy="234" r="48" fill="#cfe4f4" stroke="var(--orange)" stroke-width="5"/>
    </g>
    <g role="img" aria-label="Gloved hand wiping with a sponge">
      <circle cx="195" cy="234" r="50" fill="#e9d3c6" stroke="var(--orange)" stroke-width="5"/>
    </g>
    <g role="img" aria-label="Woman cleaning a window">
      <circle cx="365" cy="268" r="64" fill="#a9cdea" stroke="var(--orange)" stroke-width="5"/>
    </g>
    <path d="M0 452 H385 Q400 452 408 476 H758 V490 H0 Z" fill="var(--green)"/>
  </svg>

  <div class="headline headline--white">Give yourself</div>
  <div class="headline headline--orange">the gift of time</div>
  <div class="services-title">Cleaning Services for Homes<br>and Offices</div>
  <p class="services-copy">Keep your house spotless and orderly with thorough residential cleaning services from Tidy Nest Quality Cleaning Service Inc. Our professionally trained home cleaning technicians are always ready to come in and do the dirty work for you. Get in touch with us today to schedule an appointment.</p>
  <div class="front-web">www.tidynestfl.com</div>

  <div class="brand brand--front"><span class="brand__dot"></span><span class="brand__name">Tidy Nest</span></div>
  <div class="brand-sub brand-sub--front">Quality Cleaning Service, Inc.</div>
</section>

<section class="postcard postcard--back">
  <svg class="shapes" width="758" height="490" viewBox="0 0 758 490">
    <defs>
      <clipPath id="panelClip">
        <path d="M0 0 H398 Q475 245 405 490 H0 Z"/>
      </clipPath>
      <linearGradient id="topFade" x1="0" y1="0" x2="0" y2="1">
        <stop offset="0" stop-color="#ffffff"/>
        <stop offset="1" stop-color="#e4e4e4"/>
      </linearGradient>
      <linearGradient id="bandFill" x1="0" y1="0" x2="0" y2="1">
        <stop offset="0" stop-color="#1a9be0"/>
        <stop offset="1" stop-color="#0f6fc0"/>
      </linearGradient>
    </defs>
    <g clip-path="url(#panelClip)">
      <rect width="460" height="490" fill="url(#topFade)"/>
      <path d="M0 108 Q230 140 460 92 V200 H0 Z" fill="url(#bandFill)"/>
      <g role="img" aria-label="Residential living room with fireplace and armchairs">
        <rect x="0" y="204" width="218" height="143" fill="#c9a77f"/>
      </g>
      <g role="img" aria-label="Office boardroom with long wooden table">
        <rect x="225" y="204" width="240" height="143" fill="#8a5a3c"/>
      </g>
      <rect x="0" y="352" width="460" height="29" fill="var(--green)"/>
      <rect x="0" y="434" width="460" height="56" fill="var(--orange-deep)"/>
    </g>
    <path d="M398 0 Q475 245 405 490" fill="none" stroke="var(--orange)" stroke-width="6"/>
    <rect x="645" y="24" width="88" height="88" fill="var(--stamp)"/>
  </svg>

  <div class="brand brand--back"><span class="brand__dot"></span><span class="brand__name">Tidy Nest</span></div>
  <div class="brand-sub brand-sub--back">Quality Cleaning Service, Inc.</div>
  <div class="offer"><span>$25 Off</span> on Your Initial Cleaning</div>
  <div class="service-label service-label--home">Residential Cleaning</div>
  <div class="service-label service-label--office">Commercial Cleaning</div>
  <div class="estimate">Call us for a <span>free estimate</span></div>
  <div class="contact-line"><span>(555) 014-2290</span><span>www.tidynestfl.com</span></div>
</section>

</body>
</html>
```